KR Stationary Design

Logo, Business Card, Letterhead & Email Signature Design

Target Market(s)

Legal

Colors

Designer to choose colors to be used in the design.

Requirements
Must have
• Gold and Blue are the colours to use. The KR must be inside the Gold Legal Pendulum

```html
<!DOCTYPE html>
<html lang="en">
<head>
<meta charset="utf-8">
<title>Kendrick Rowe Attorneys – Business Card</title>
<link rel="stylesheet" href="https://fonts.googleapis.com/css2?family=Noto+Serif:wght@400&family=Roboto:wght@400&display=swap">
<style>
  :root {
    --navy: #13284f;
    --gold: #c9a82c;
    --white: #ffffff;
    --ink: #3a3a3a;
    --backdrop: #c4c5c9;
  }
  * { margin: 0; padding: 0; box-sizing: border-box; }
  html, body { width: 1200px; height: 852px; overflow: hidden; }
  body {
    background: var(--backdrop);
    position: relative;
    font-family: "Roboto", Arial, sans-serif;
  }
  .card {
    position: absolute;
    top: 272px;
    width: 540px;
    height: 308px;
  }
  .card--front { left: 40px; background: var(--navy); }
  .card--back { left: 620px; background: var(--white); }

  .brand {
    position: absolute;
    display: flex;
    align-items: center;
    gap: 12px;
    font-family: "Noto Serif", Georgia, serif;
    font-weight: 400;
    letter-spacing: 1px;
    text-transform: uppercase;
    white-space: nowrap;
  }
  .brand__dot { border-radius: 50%; flex: none; }
  .card--front .brand {
    left: 50%; top: 50%;
    transform: translate(-50%, -50%);
    color: var(--white);
    font-size: 26px;
  }
  .card--front .brand__dot { width: 40px; height: 40px; background: var(--gold); }
  .card--back .brand {
    right: 36px; top: 34px;
    color: var(--navy);
    font-size: 17px;
  }
  .card--back .brand__dot { width: 28px; height: 28px; background: var(--gold); }

  .address {
    position: absolute;
    right: 36px; top: 92px;
    text-align: right;
    font-size: 12.5px;
    line-height: 1.4;
    color: var(--ink);
  }
  .holder {
    position: absolute;
    left: 36px; bottom: 36px;
  }
  .holder__name {
    font-family: "Noto Serif", Georgia, serif;
    font-size: 21px;
    color: var(--navy);
    text-transform: uppercase;
    letter-spacing: 0.5px;
  }
  .holder__role {
    font-size: 14px;
    color: var(--gold);
    margin-top: 2px;
  }
  .holder__rule {
    width: 22px; height: 4px;
    background: var(--navy);
    margin: 10px 0 10px;
  }
  .contact { list-style: none; font-size: 13px; color: var(--ink); line-height: 1.55; }
  .contact li { display: flex; align-items: center; gap: 8px; }
  .contact svg { width: 12px; height: 12px; fill: var(--navy); flex: none; }
</style>
</head>
<body>
  <section class="card card--front">
    <div class="brand"><span class="brand__dot"></span>Kendrick Rowe Attorneys</div>
  </section>

  <section class="card card--back">
    <div class="brand"><span class="brand__dot"></span>Kendrick Rowe Attorneys</div>
    <address class="address" style="font-style:normal">
      Unit 4 Larchwood Office Park<br>
      22 Elmstead road north<br>
      Rivonia, 2128
    </address>
    <div class="holder">
      <p class="holder__name">Kai Rowe</p>
      <p class="holder__role">Director</p>
      <div class="holder__rule"></div>
      <ul class="contact">
        <li><svg viewBox="0 0 12 12"><path d="M2 1h2.5l1 3-1.5 1a7 7 0 0 0 3 3l1-1.5 3 1V10a1 1 0 0 1-1 1A9 9 0 0 1 1 2a1 1 0 0 1 1-1z"/></svg>011 402 7781</li>
        <li><svg viewBox="0 0 12 12"><rect x="3" y="1" width="6" height="3"/><rect x="1" y="4.5" width="10" height="4.5" rx="1"/><rect x="3" y="8" width="6" height="3"/></svg>086 319 4560</li>
        <li><svg viewBox="0 0 12 12"><path d="M1 2.5h10v7H1z M1 2.5l5 4 5-4" stroke="#fff" stroke-width="0.8"/></svg>kai@krowe-law.co.za</li>
      </ul>
    </div>
  </section>
</body>
</html>
```